Need UI design for an iOS app game with most of the layout planned

The name of the game is "QUADRIX".

The goal of the game is to find a way to manipulate four numbers so that the end result is 24. Addition, subtraction, multiplication and division may be used and each number can only be used once.

The list of items we need is:

1. launch image, app icon, UI design of all scenes (10-12 scenes) of the app.
2. App background image should support screen size of both 640x1136.
3. Files are preferred to be in (.eps) format so that resolution can be adjusted later. But other file formats are welcome as long as resolution is high enough.
4. Icons, buttons, background image etc. should have their own file so that later they can be moved around in case design is changed.

The detailed requirement is in the attached file. The actual layout can vary if it can help achieve better result. We also attached several screenshots from iOS game "Glimbo". You can use that as your reference.

```html
<!DOCTYPE html>
<html lang="en">
<head>
<meta charset="utf-8">
<title>QUADRIX – Home</title>
<link rel="stylesheet" href="https://fonts.googleapis.com/css2?family=Arimo:wght@700&display=swap">
<style>
  :root {
    --bg-center: #5fc0f5;
    --bg-mid: #2a8ee0;
    --bg-edge: #1566c4;
    --corner-blue: #1d6fd0;
    --corner-dark: #0f4a9a;
    --orange-top: #ffa233;
    --orange-bottom: #f27a0c;
    --orange-edge: #c25800;
    --icon-fill: #ffd9b0;
    --white: #ffffff;
    --title-orange: #f48a12;
  }
  * { margin: 0; padding: 0; box-sizing: border-box; }
  html, body { width: 677px; height: 1200px; overflow: hidden; }
  body {
    position: relative;
    font-family: "Arimo", Arial, sans-serif;
    background: radial-gradient(ellipse at 50% 62%, var(--bg-center) 0%, var(--bg-mid) 45%, var(--bg-edge) 100%);
  }
  .corner-button {
    position: absolute;
    top: -50px;
    width: 144px;
    height: 144px;
    border-radius: 50%;
    background: radial-gradient(circle at 60% 65%, var(--corner-blue), var(--corner-dark));
    box-shadow: 0 4px 10px rgba(0,0,0,.35);
  }
  .corner-button svg { position: absolute; }
  .settings-button { left: -54px; }
  .settings-button svg { left: 66px; top: 68px; }
  .info-button { right: -54px; }
  .info-label {
    position: absolute;
    left: 36px;
    top: 56px;
    color: var(--white);
    font-style: italic;
    font-size: 54px;
    font-family: Georgia, serif;
  }
  .game-title {
    position: absolute;
    left: 0;
    right: 0;
    top: 370px;
    text-align: center;
    font-size: 118px;
    font-weight: 700;
    color: var(--title-orange);
    letter-spacing: 2px;
  }
  .menu-button {
    position: absolute;
    left: 63px;
    width: 569px;
    height: 158px;
    border-radius: 10px;
    background: linear-gradient(var(--orange-top), var(--orange-bottom));
    box-shadow: inset 0 -14px 0 var(--orange-edge), 0 6px 12px rgba(0,0,0,.3);
    display: flex;
    align-items: center;
    padding-bottom: 12px;
  }
  .single-button { top: 673px; }
  .multi-button { top: 885px; }
  .player-icon {
    flex: none;
    margin-left: 28px;
    height: 104px;
    border-radius: 8px;
    background: linear-gradient(var(--icon-fill), #f6b26a);
    opacity: .85;
  }
  .single-button .player-icon { width: 100px; }
  .multi-button .player-icon { width: 150px; margin-left: 24px; }
  .menu-label {
    color: var(--white);
    font-size: 50px;
    font-weight: 700;
    margin-left: 34px;
    text-shadow: 0 2px 2px rgba(0,0,0,.25);
  }
  .multi-button .menu-label { margin-left: 20px; }
</style>
</head>
<body>
  <div class="corner-button settings-button" aria-label="Settings">
    <svg width="52" height="52" viewBox="0 0 52 52">
      <g fill="var(--white)" transform="translate(26 26)">
        <rect x="-5" y="-25" width="10" height="12" rx="2"/>
        <rect x="-5" y="-25" width="10" height="12" rx="2" transform="rotate(45)"/>
        <rect x="-5" y="-25" width="10" height="12" rx="2" transform="rotate(90)"/>
        <rect x="-5" y="-25" width="10" height="12" rx="2" transform="rotate(135)"/>
        <rect x="-5" y="-25" width="10" height="12" rx="2" transform="rotate(180)"/>
        <rect x="-5" y="-25" width="10" height="12" rx="2" transform="rotate(225)"/>
        <rect x="-5" y="-25" width="10" height="12" rx="2" transform="rotate(270)"/>
        <rect x="-5" y="-25" width="10" height="12" rx="2" transform="rotate(315)"/>
        <circle r="17"/>
      </g>
      <circle cx="26" cy="26" r="7" fill="var(--corner-blue)"/>
    </svg>
  </div>
  <div class="corner-button info-button" aria-label="Information">
    <span class="info-label">i</span>
  </div>

  <h1 class="game-title">QUADRIX</h1>

  <div class="menu-button single-button">
    <div class="player-icon" role="img" aria-label="Single player figure icon"></div>
    <span class="menu-label">Single Players</span>
  </div>
  <div class="menu-button multi-button">
    <div class="player-icon" role="img" aria-label="Group of three players icon"></div>
    <span class="menu-label">Multi Players</span>
  </div>
</body>
</html>
```